Design our next "BOLD HORIZON" print. Size 12x36 Horizontal.

I am looking for a poster design with the text "Bold Horizon" . The print size will be a 12x36 inches.(Horizontal) It should have the American flag used throughout the design. I am looking for a very proud feeling. Font can be creative but instantly readable. The design can be old world feel and can also use the deep reds and navy blues.The image does not have to be just the flag and text. It can contain other patriotic symbols. Can also have a grungy feel. I have enclosed our last "Bold Horizon " piece for your reference. We are hoping we can get one even better. Thank You.

• Should Not be like the image example I enclosed. It's just a reference. We need something that is new and different. Plain White text.

```html
<!DOCTYPE html>
<html lang="en">
<head>
<meta charset="utf-8">
<title>Bold Horizon Print</title>
<link rel="stylesheet" href="https://fonts.googleapis.com/css2?family=Libre+Franklin:wght@800&display=swap">
<style>
  :root {
    --flag-red: #d4232b;
    --flag-white: #f4f1f0;
    --flag-navy: #1f4fae;
    --flag-navy-deep: #0f2f7d;
    --title-ink: #16182a;
    --page: #ffffff;
  }
  html, body {
    margin: 0;
    padding: 0;
    width: 1200px;
    height: 400px;
    overflow: hidden;
    background: var(--page);
  }
  .poster {
    display: block;
    width: 1200px;
    height: 400px;
  }
  .stripe-red { fill: var(--flag-red); }
  .stripe-white { fill: var(--flag-white); }
  .title {
    font-family: "Libre Franklin", "Helvetica Neue", Arial, sans-serif;
    font-weight: 800;
    font-size: 150px;
    fill: var(--title-ink);
  }
</style>
</head>
<body>
<svg class="poster" viewBox="0 0 1200 400" xmlns="http://www.w3.org/2000/svg">
  <defs>
    <linearGradient id="cantonTone" x1="0" y1="0" x2="1" y2="1">
      <stop offset="0" stop-color="var(--flag-navy-deep)"/>
      <stop offset="0.6" stop-color="var(--flag-navy)"/>
      <stop offset="1" stop-color="#8fa6d8"/>
    </linearGradient>
    <radialGradient id="centreWash" cx="0.5" cy="0.5" r="0.6">
      <stop offset="0" stop-color="#ffffff" stop-opacity="0.35"/>
      <stop offset="1" stop-color="#ffffff" stop-opacity="0"/>
    </radialGradient>
  </defs>

  <g class="flag-field">
    <rect class="stripe-red" x="0" y="0" width="1200" height="55"/>
    <rect class="stripe-white" x="0" y="55" width="1200" height="50"/>
    <rect class="stripe-red" x="0" y="105" width="1200" height="50"/>
    <rect class="stripe-white" x="0" y="155" width="1200" height="50"/>
    <rect class="stripe-red" x="0" y="205" width="1200" height="50"/>
    <rect class="stripe-white" x="0" y="255" width="1200" height="50"/>
    <rect class="stripe-red" x="0" y="305" width="1200" height="40"/>
    <rect class="stripe-white" x="0" y="345" width="1200" height="10"/>
    <rect class="stripe-red" x="0" y="355" width="1200" height="45"/>
    <rect class="flag-canton" x="0" y="0" width="552" height="290" fill="url(#cantonTone)"
          role="img" aria-label="Blue flag canton with white stars in a watercolour grunge wash"/>
    <rect class="flag-wash" x="0" y="0" width="1200" height="400" fill="url(#centreWash)"/>
  </g>

  <text class="title" x="600" y="255" text-anchor="middle" textLength="1110" lengthAdjust="spacing">BOLD HORIZON</text>
</svg>
</body>
</html>
```